Card for Real Estate Developer

We need a business card design for a Real Estate Development company based in Texas. We focus on retail, apartment and residential development. Our target is predominantly investors looking to us to place their money properly to achieve a significant return. On the other side we sell our services to large retailers as their preferred developer assisting them in locating, building and leasing their real estate.

Target Market(s)

Investors

Industry/Entity Type

Real Estate Development

Contact Information for Business Card

Would like to stay within the company color scheme, while keeping the design moderately simple.

Font styles to use
Other font styles liked:
• per attached document

Requirements
Must have
• Name
• Phone
• Email
• Website
• Logo Prominently Displayed
• Stay within the colors provided in the attached document

```html
<!DOCTYPE html>
<html lang="en">
<head>
<meta charset="utf-8">
<title>Halvern Development — Business Card</title>
<link href="https://fonts.googleapis.com/css2?family=Open+Sans:wght@400;600;700&display=swap" rel="stylesheet">
<style>
  :root {
    --backdrop: #9a9a9a;
    --card-white: #ffffff;
    --brand-navy: #0f4a7c;
    --brand-sky: #4a9fd0;
    --ink: #1a1a1a;
    --ink-soft: #333333;
    --icon-grey: #555555;
  }
  * { margin: 0; padding: 0; box-sizing: border-box; }
  html, body {
    width: 1200px;
    height: 960px;
    overflow: hidden;
    background: var(--backdrop);
    font-family: "Open Sans", Arial, sans-serif;
  }
  .sheet {
    width: 1200px;
    height: 960px;
    display: flex;
    align-items: center;
    justify-content: center;
    gap: 40px;
  }
  .card {
    width: 540px;
    height: 309px;
    position: relative;
    box-shadow: 0 10px 24px rgba(0,0,0,0.25);
  }

  /* Back side */
  .card-back {
    background: linear-gradient(160deg, #17578f 0%, var(--brand-navy) 60%, #0c3f6b 100%);
    display: flex;
    align-items: center;
    justify-content: center;
    gap: 18px;
  }
  .card-back .brand-square {
    width: 34px;
    height: 34px;
    background: var(--card-white);
  }
  .card-back .brand-name {
    color: var(--card-white);
    font-weight: 600;
    font-size: 40px;
    letter-spacing: 4px;
    text-transform: uppercase;
  }

  /* Front side */
  .card-front {
    background: var(--card-white);
  }
  .front-brand {
    position: absolute;
    left: 40px;
    top: 62px;
    display: flex;
    align-items: center;
    gap: 14px;
  }
  .front-brand .brand-square {
    width: 26px;
    height: 26px;
    background: var(--brand-sky);
  }
  .front-brand .brand-name {
    color: var(--ink);
    font-weight: 600;
    font-size: 24px;
    letter-spacing: 2px;
    text-transform: uppercase;
    line-height: 1.25;
  }
  .front-rule {
    position: absolute;
    left: 40px;
    top: 140px;
    width: 230px;
    height: 2px;
    background: var(--ink);
  }
  .contact {
    position: absolute;
    left: 300px;
    top: 150px;
    color: var(--ink-soft);
  }
  .contact .person-name {
    font-weight: 700;
    font-size: 20px;
    color: var(--ink);
    margin-bottom: 12px;
  }
  .contact .line {
    display: flex;
    align-items: center;
    gap: 8px;
    font-size: 13px;
    margin-bottom: 5px;
  }
  .contact .line svg { width: 11px; height: 11px; fill: var(--icon-grey); }
  .contact .website {
    font-size: 13px;
    margin-top: 10px;
  }
  .contact .website strong { font-weight: 700; color: var(--ink); }
</style>
</head>
<body>
  <main class="sheet">
    <section class="card card-back" aria-label="Card back">
      <span class="brand-square"></span>
      <span class="brand-name">Halvern</span>
    </section>

    <section class="card card-front" aria-label="Card front">
      <div class="front-brand">
        <span class="brand-square"></span>
        <span class="brand-name">Halvern<br>Development</span>
      </div>
      <div class="front-rule"></div>

      <div class="contact">
        <p class="person-name">Reed Calloway</p>
        <p class="line">
          <svg viewBox="0 0 24 24" aria-hidden="true"><path d="M6.6 10.8a15.1 15.1 0 0 0 6.6 6.6l2.2-2.2a1 1 0 0 1 1-.25 11.4 11.4 0 0 0 3.6.57 1 1 0 0 1 1 1V20a1 1 0 0 1-1 1A17 17 0 0 1 3 4a1 1 0 0 1 1-1h3.5a1 1 0 0 1 1 1c0 1.25.2 2.45.57 3.57a1 1 0 0 1-.25 1z"/></svg>
          979-555-0148
        </p>
        <p class="line">
          <svg viewBox="0 0 24 24" aria-hidden="true"><path d="M2 5h20v14H2z M2 5l10 8 10-8" /></svg>
          rcalloway@halvernco.com
        </p>
        <p class="website">www.<strong>halvernco</strong>.com</p>
      </div>
    </section>
  </main>
</body>
</html>
```